依頼詳細
開設告知を病院や行政、居宅介護支援事業所に行うための簡易的なチラシの作成をお願いいたします。情報量は最低限で、雰囲気重視、まずは時期と場所をしっかりと伝えて初期段階の営業を行うためのツールを想定しています。
記載項目
別紙資料をご確認ください。
サイズ
A4
ページ数
片面
希望イメージ
シンプル 複雑
単色 カラフル
暗い 明るい
日常 高級
遊び心 厳粛
未来的 伝統的
女性的 男性的
希望する色
納品ファイル
補足説明

スタッフの投票で決めました。

大変すばらしい提案をいただきましてありがとうございました。今後もパンフレット等、様々依頼をさせていただく予定ですので、今後とも宜しくお願い致します。

```html
<!DOCTYPE html>
<html lang="ja">
<head>
<meta charset="UTF-8">
<title>住宅型有料老人ホーム つきあかり 月灯 開設のお知らせ</title>
<link rel="stylesheet" href="https://fonts.googleapis.com/css2?family=Noto+Sans+JP:wght@400;500;700&family=Noto+Serif+JP:wght@500;700&display=swap">
<style>
:root{
  --green:#5aa33a;
  --green-dark:#3f8526;
  --green-pale:#e9f3df;
  --navy:#2a3b6e;
  --ink:#333;
  --muted:#666;
  --line:#c9d9bb;
  --white:#fff;
}
*{margin:0;padding:0;box-sizing:border-box}
html,body{width:846px;height:1200px;overflow:hidden;background:var(--white)}
body{font-family:"Noto Sans JP",sans-serif;color:var(--ink)}
.flyer{position:relative;width:846px;height:1200px;overflow:hidden;background:var(--white)}

/* hero */
.hero{position:absolute;left:0;top:0;width:846px;height:540px;
  background:
    radial-gradient(circle at 14% 12%,rgba(255,255,255,.8) 0,rgba(255,255,255,0) 18%),
    radial-gradient(circle at 86% 10%,rgba(255,255,255,.7) 0,rgba(255,255,255,0) 20%),
    linear-gradient(180deg,#86c057 0%,#a4d178 45%,#cfe6b3 80%,#e4efd7 100%);}
.hero-people{position:absolute;top:0;height:540px;border-radius:0}
.hero-people.left{left:0;width:300px;
  background:
    radial-gradient(ellipse at 30% 40%,rgba(245,232,214,.95) 0,rgba(245,232,214,0) 40%),
    radial-gradient(ellipse at 55% 78%,rgba(250,250,248,.95) 0,rgba(250,250,248,0) 50%),
    radial-gradient(ellipse at 15% 80%,rgba(238,226,210,.9) 0,rgba(238,226,210,0) 40%);}
.hero-people.right{right:0;width:300px;
  background:
    radial-gradient(ellipse at 40% 50%,rgba(240,228,214,.95) 0,rgba(240,228,214,0) 40%),
    radial-gradient(ellipse at 82% 40%,rgba(247,238,228,.95) 0,rgba(247,238,228,0) 38%),
    radial-gradient(ellipse at 50% 85%,rgba(226,214,224,.9) 0,rgba(226,214,224,0) 45%);}
.hero-glow{position:absolute;left:233px;top:20px;width:380px;height:340px;border-radius:50%;
  background:radial-gradient(ellipse at center,rgba(255,255,255,.55) 0,rgba(255,255,255,0) 70%)}
.hero-title{position:absolute;left:0;top:60px;width:846px;text-align:center;color:var(--white);text-shadow:0 1px 6px rgba(40,90,20,.45)}
.hero-title .mark{display:block;margin:0 auto 22px;width:110px;height:110px;border-radius:50%;border:3px solid rgba(255,255,255,.9)}
.hero-title .kind{font-family:"Noto Serif JP",serif;font-size:19px;letter-spacing:.16em;font-weight:500}
.hero-title .name{font-family:"Noto Serif JP",serif;font-size:58px;font-weight:700;letter-spacing:.12em;line-height:1.15;margin-top:2px}
.hero-title .name-kanji{font-family:"Noto Serif JP",serif;font-size:22px;letter-spacing:1.6em;font-weight:500;margin-top:2px;padding-left:1.6em}
.opening{position:absolute;left:0;top:406px;width:846px;text-align:center;color:var(--white);font-family:"Noto Serif JP",serif;text-shadow:0 1px 8px rgba(40,80,20,.5)}
.opening .date{font-size:36px;font-weight:700;letter-spacing:.04em;line-height:1.2}
.opening .open{font-size:70px;font-weight:700;letter-spacing:.06em;line-height:1.1}

/* features */
.features{position:absolute;left:30px;top:556px;width:786px;display:grid;grid-template-columns:repeat(4,1fr);column-gap:14px}
.feature p{font-size:12.5px;line-height:1.65;height:118px;color:var(--ink)}
.feature .photo{height:122px;border-radius:2px}
.photo-park{background:linear-gradient(160deg,#9fcf6c,#5d9a3c)}
.photo-rehab{background:linear-gradient(160deg,#f1ede6,#c9d8e6)}
.photo-theater{background:linear-gradient(160deg,#cfe0ef,#8fb06a)}
.photo-garden{background:linear-gradient(160deg,#7fbf58,#3d7d2a)}

/* services & prices */
.services{position:absolute;left:30px;top:822px;width:186px;font-size:13px;line-height:1.8;color:var(--green-dark);font-weight:500;list-style:none}
.prices{position:absolute;left:230px;top:818px;width:586px}
.prices-head{background:var(--green);color:var(--white);font-size:14px;font-weight:700;padding:3px 12px;letter-spacing:.3em}
.prices-table{display:grid;grid-template-columns:repeat(4,1fr);border:1px solid var(--line);border-top:none}
.price{padding:8px 10px;display:flex;align-items:baseline;gap:10px;border-right:1px solid var(--line);white-space:nowrap}
.price:last-child{border-right:none}
.price .label{font-size:13px;color:var(--muted)}
.price .value{font-size:19px;font-weight:700;color:var(--ink)}
.price .value small{font-size:12px;font-weight:500}
.price.total{background:var(--green-pale)}
.prices-note{font-size:11px;color:var(--muted);text-align:right;margin-top:6px}

/* contact */
.contact{position:absolute;left:30px;top:958px;width:786px;height:210px;border-top:2px solid var(--green)}
.brand{position:absolute;left:0;top:24px;width:160px;text-align:center;color:var(--navy)}
.brand .dot{display:block;margin:0 auto 8px;width:22px;height:22px;border-radius:50%;background:var(--navy)}
.brand .name{font-family:"Noto Serif JP",serif;font-size:28px;font-weight:700;letter-spacing:0;line-height:1.15;white-space:nowrap}
.brand .sub{font-family:"Noto Serif JP",serif;font-size:15px;letter-spacing:.5em;padding-left:.5em;margin-top:4px}
.office{position:absolute;left:180px;top:18px;width:320px}
.office .dept{font-size:15px;font-weight:700;color:var(--navy)}
.office .tel{display:flex;align-items:center;gap:8px;font-size:38px;font-weight:700;color:var(--navy);line-height:1.15;letter-spacing:.02em;white-space:nowrap}
.office .tel svg{width:30px;height:30px}
.office .address{font-size:13px;color:var(--ink);margin-top:4px;white-space:nowrap}
.access{position:absolute;left:180px;top:128px;width:320px;background:var(--green);color:var(--white);padding:8px 12px;font-size:13.5px;line-height:1.5;font-weight:500;white-space:nowrap}
.access strong{font-size:18px;color:#fff9c8}
.map{position:absolute;left:520px;top:14px;width:266px;height:186px;background:linear-gradient(135deg,#f3f5ef,#dfe9d4);border:1px solid var(--line)}
</style>
</head>
<body>
<main class="flyer">
  <section class="hero" role="img" aria-label="緑あふれる屋外で介護スタッフと笑顔の高齢者たちの写真">
    <div class="hero-people left"></div>
    <div class="hero-people right"></div>
    <div class="hero-glow"></div>
  </section>
  <header class="hero-title">
    <span class="mark"></span>
    <div class="kind">住宅型有料老人ホーム</div>
    <div class="name">つきあかり</div>
    <div class="name-kanji">月灯</div>
  </header>
  <div class="opening">
    <div class="date">2021年4月</div>
    <div class="open">OPEN</div>
  </div>

  <section class="features">
    <article class="feature">
      <p>若葉沼ふれあい公園<br>徒歩1分。<br>自然豊かで<br>落ち着いたホームです。</p>
      <div class="photo photo-park" role="img" aria-label="公園の緑と住宅の写真"></div>
    </article>
    <article class="feature">
      <p>理学療法士、<br>作業療法士を配置し、<br>機能回復訓練に力を<br>入れています。<br>できることを増やしましょう。</p>
      <div class="photo photo-rehab" role="img" aria-label="機能訓練の様子の写真"></div>
    </article>
    <article class="feature">
      <p>シアタールーム等、<br>余暇活動が<br>充実しています。</p>
      <div class="photo photo-theater" role="img" aria-label="シアタールームでの余暇活動の写真"></div>
    </article>
    <article class="feature">
      <p>様々な園芸スペースも<br>あります。<br>認知機能向上のため<br>植物の栽培を<br>楽しみましょう。</p>
      <div class="photo photo-garden" role="img" aria-label="園芸スペースの植物の写真"></div>
    </article>
  </section>

  <ul class="services">
    <li>■ 訪問介護事業所</li>
    <li>■ 通所介護事業所</li>
  </ul>

  <section class="prices">
    <div class="prices-head">費用</div>
    <div class="prices-table">
      <div class="price"><span class="label">家賃</span><span class="value">27,000<small>円〜</small></span></div>
      <div class="price"><span class="label">食費</span><span class="value">39,000<small>円</small></span></div>
      <div class="price"><span class="label">管理費</span><span class="value">18,000<small>円</small></span></div>
      <div class="price total"><span class="label">合計</span><span class="value">84,000<small>円〜</small></span></div>
    </div>
    <p class="prices-note">お部屋のタイプによって金額が異なる場合があります。</p>
  </section>

  <footer class="contact">
    <div class="brand">
      <span class="dot"></span>
      <div class="name">つきあかり</div>
      <div class="sub">月灯</div>
    </div>
    <div class="office">
      <div class="dept">開設準備室</div>
      <div class="tel">
        <svg viewBox="0 0 24 24" aria-hidden="true"><path fill="currentColor" d="M6.6 10.8a15.1 15.1 0 0 0 6.6 6.6l2.2-2.2a1 1 0 0 1 1-.25 11.4 11.4 0 0 0 3.6.57 1 1 0 0 1 1 1V20a1 1 0 0 1-1 1A17 17 0 0 1 3 4a1 1 0 0 1 1-1h3.5a1 1 0 0 1 1 1 11.4 11.4 0 0 0 .57 3.6 1 1 0 0 1-.25 1z"/></svg>
        000-000-0000
      </div>
      <div class="address">〒100-0000 北野県緑川市若葉町1234-5</div>
    </div>
    <div class="access">中央緑川自動車道若葉ICから車で<strong>1分</strong><br>高速道路からのアクセス抜群</div>
    <div class="map" role="img" aria-label="施設周辺の案内地図"></div>
  </footer>
</main>
</body>
</html>
```